Compass & Canvas needs new business card design

I need a new business card design. I'm looking for out-of-the-box design which represents the freedom of being a location independent entrepreneur.
I offer coaching, retreats and trips.
I would like to see designs with and without the photo.
Colors I use are black (#000000), green (#25A796) and brown (#D7C38C)
Website compassandcanvas.net

Target Market(s)

location independent entrepreneurs, digital nomads, people looking to swap the 9 to 5 for a lifestyle business

Industry/Entity Type

Business

Contact Information for Business Card

Daria Tolsen
Your Lifestyle Business Coach, Retreat & Trip Leader
http://compassandcanvas.net
hello@compassandcanvas.net
Live a life you don't need a holiday from

Font styles to use
Serif
Sans Serif

Requirements
Must have
• One side should contain only the logo. I would also consider having the "Live a life you don't need a holiday from" on that side too (depending on how it looks)
• Please show both sides on the designs.

```html
<!DOCTYPE html>
<html lang="en">
<head>
<meta charset="utf-8">
<title>Compass &amp; Canvas – Business Card, Front and Back</title>
<link rel="stylesheet" href="https://fonts.googleapis.com/css2?family=Kalam:wght@400;700&display=swap">
<style>
  :root {
    --ink: #1e1d1f;
    --ink-soft: #2a292c;
    --green: #25a796;
    --white: #ffffff;
    --clear: rgba(226, 236, 242, 0.55);
    --clear-edge: rgba(255, 255, 255, 0.7);
    --bg-top: #a9b9c4;
    --bg-mid: #c6d2da;
    --bg-bottom: #98a9b5;
  }
  * { margin: 0; padding: 0; box-sizing: border-box; }
  html, body { width: 1200px; height: 792px; overflow: hidden; }
  body {
    position: relative;
    background: linear-gradient(90deg, var(--bg-top) 0%, var(--bg-mid) 50%, var(--bg-bottom) 100%);
    font-family: "Kalam", cursive;
  }
  .card {
    position: absolute;
    top: 232px;
    width: 523px;
    height: 333px;
    border-radius: 16px;
    overflow: hidden;
    background: var(--clear);
    border: 1px solid var(--clear-edge);
  }
  .card--front { left: 55px; }
  .card--back { left: 625px; }
  .card__shapes { position: absolute; inset: 0; width: 100%; height: 100%; }

  .brand-name {
    position: absolute;
    font-family: "Kalam", cursive;
    font-weight: 700;
    font-size: 33px;
    letter-spacing: 1px;
    line-height: 1;
    white-space: nowrap;
    text-transform: uppercase;
  }
  .card--front .brand-name { left: 30px; top: 232px; color: var(--white); }
  .card--back .brand-name {
    left: 110px; top: 163px;
    color: var(--ink);
    transform: translate(-50%, -50%) rotate(-57deg);
  }

  .contact {
    position: absolute;
    right: 30px;
    top: 143px;
    text-align: right;
    color: var(--white);
  }
  .contact__name { color: var(--green); font-weight: 700; font-size: 18px; line-height: 1.2; letter-spacing: 0.5px; }
  .contact__role { font-size: 11.5px; font-weight: 700; line-height: 1.35; }
  .contact__links { margin-top: 16px; font-size: 13px; font-weight: 700; line-height: 1.3; }
  .tagline {
    position: absolute;
    right: 30px;
    bottom: 36px;
    color: var(--green);
    font-size: 12px;
    font-weight: 700;
    letter-spacing: 0.4px;
  }
</style>
</head>
<body>

  <section class="card card--front" aria-label="Card front">
    <svg class="card__shapes" viewBox="0 0 523 333" aria-hidden="false">
      <polygon points="0,0 155,0 355,333 0,333" fill="var(--ink)"/>
      <polygon points="0,0 150,0 240,150 0,230" fill="var(--ink-soft)" role="img" aria-label="Faint background photo of the coach working with a laptop"/>
      <polygon points="155,0 210,0 415,333 355,333" fill="var(--green)"/>
    </svg>
    <div class="brand-name">Compass &amp; Canvas</div>
  </section>

  <section class="card card--back" aria-label="Card back">
    <svg class="card__shapes" viewBox="0 0 523 333">
      <polygon points="365,0 523,0 523,333 165,333" fill="var(--ink)"/>
      <polygon points="310,0 365,0 165,333 110,333" fill="var(--green)"/>
    </svg>
    <div class="brand-name">Compass &amp; Canvas</div>
    <div class="contact">
      <p class="contact__name">Daria Tolsen</p>
      <p class="contact__role">Your Lifestyle Business Coach ,<br>Retreat &amp; Trip Leader</p>
      <p class="contact__links">http://compassandcanvas.net<br>hello@compassandcanvas.net</p>
    </div>
    <p class="tagline">Live a life you don't need a holiday from</p>
  </section>

</body>
</html>
```